Create the BEST and COOLEST website for events and media company!

Hi there. I am a start-up events and conferences company with a twist, and we are seeking a highly modern website for our company Quillfern Media. Our company believes that (like the social networking theory) that each and every one of us is connected to anyone on the planet in six connections or less. E.g. I know someone, who knows someone, who knows someone. Hence, the name Quillfern Media.

I have included the copy for the website attached.

While we do have a business audience, they are in the fields of technology from the banking, health, government sector. We would like our website to be edgy, fresh and steer away from stuffy corporate images.

To give you an idea, our website menu tabs will be labelled:
HOME: This will include a corporate video that’s being created next week for me. However, please still design this page with a very striking background image that fills the whole page. You can run the copy and put a mock video for me to just see the layout (we can insert the finished video later).

ROCKSTARS: this will show pictures of highly powerful leaders speaking on stage; with a highly engaged audience watching. We want to show we have the world’s best technology International speakers “rockstars” who are the best in their game when it comes to talking about the future of technology.

LOCAL LEGENDS: like the international ‘rockstar’ speakers we would bring over to Australia to present; this LOCAL LEGENDS page should show we have the best home-grown Chief business people speaking at conferences and smaller powerful roundtable luncheons.

UNSUNG HEROES: this is more the people in the audience who ask questions on a microphone; those that attend the conferences; or a speaking to people at a conference.

THE BAND: this is like an ‘about us’ – just a funkier name to tie in with the theme of rockstars, etc.

THE PARTNERS: this is like a sponsor client page, where we invite people to partner with us and sponsor our events and conferences.

YOU & DORIAN PELLHAM: Dorian Pellham is a famous actor who made the term ‘six degrees of separation’ very popular. This page will have a little bit of an introduction, but mainly have the following video fill the landing page: https://www.vidplume.example/watch?v=Tq4-zLp8XwE

Website Functionality and Features:

• Try and make the ‘vibe’ and look and feel consistent, hip and modern (but still maintain a professional look). At the end of the day, people looking at our website are very senior business chiefs of organisations and also marketing chiefs.
• We may add more pages once we become established, so the website needs to ensure we can do that easily.
• We want pictures to not look stock photos. We want them to fresh, innovative, inspirational.
• Images should have a ‘wow’ factor. Like this one: https://www.picharbor.example/detail/news-photo/general-view-of-atmosphere-during-brightloom-talks-2018-from-me-news-photo/481253907
• Need a mix of speaker, stage, audience, pictures. While we want to be fresh, edgy and contemporary we need to remember our viewers are the big chiefs of businesses – so lets try and have cool shots, but ensure there is a link to the business decision makers in a modern way. They all don’t have to wear suits, but not too casual either
• Other types of imagery I like is this one: https://www.picharbor.example/detail/photo/smiling-audience-using-smart-phone-flashlights-for-royalty-free-image/362817045.
• The following are ok, not wow – but to give you an idea:
• https://www.picharbor.example/detail/photo/smiling-male-speaker-in-wheelchair-on-stage-royalty-free-image/362819531
https://www.picharbor.example/detail/photo/smiling-woman-with-camera-phone-in-dark-audience-royalty-free-image/362818476
https://www.picharbor.example/detail/photo/audience-using-camera-phones-royalty-free-image/367402158
https://www.picharbor.example/detail/photo/male-speaker-on-stage-talking-to-audience-royalty-free-image/362818893

NB: Logos are supplied in low resolution, but I can send you high resolution also
Updates

Hi there I will be adding two low-resolution images of my business partner and I for the ABOUT US page which is called THE BAND in the menu tab.

Hi everyone, thank you for your designs. I have uploaded a MAIN SCREEN IDEAS word document to give you further ideas of how the options I like for the main landing page on the home page. Hope this helps!

Target Market(s)

High end business people in marketing and business.

Coding

Coded - Design and coding required

Number of Pages Required

5+ page

Font styles to use
Sans Serif

Requirements
Must have
• Fresh, inspirational and aspirational designs. We need to make events and conferences look exciting and that we are bring the best technology speakers (like Brightloom events) to our audience of marketing and technology professionals.
Should not have
• Cheesy, old stock photos; or pictures of American executives as this is for an Australian audience.
• PLEASE do not include an UPCOMING EVENTS or a SPEAKERS section as we will not be having this showcasing. You can feature ROCK STARS, LOCAL LEGENDS and UNSUNG HEROES if you like on the home page + the video of YOU and DORIAN PELLHAM (with his picture on the video box with a play button)

```html
<!DOCTYPE html>
<html lang="en">
<head>
<meta charset="utf-8">
<title>Quillfern Media — Events and Conferences</title>
<link href="https://fonts.googleapis.com/css2?family=Roboto:wght@300;400;500;700&family=Roboto+Condensed:wght@400;700&display=swap" rel="stylesheet">
<style>
:root{
  --blue:#1bbde0;
  --blue-dark:#12a6c7;
  --ink:#1f1f1f;
  --text:#4a4a4a;
  --muted:#777;
  --charcoal:#3a3a3a;
  --night:#2a2a2a;
  --line:#e3e3e3;
  --fb:#3b5998;
  --red:#e0201b;
  --white:#fff;
}
*{margin:0;padding:0;box-sizing:border-box}
html,body{width:1200px;height:3750px;overflow:hidden}
body{position:relative;background:var(--white);font-family:"Roboto",Arial,sans-serif;color:var(--text)}
.abs{position:absolute}
.center{text-align:center}
p{font-size:11px;line-height:16px;color:var(--text)}
.btn{position:absolute;display:flex;align-items:center;justify-content:center;font-size:12px;font-weight:500;letter-spacing:.5px;color:var(--white);text-transform:uppercase}
.btn-blue{background:var(--blue)}
.btn-dark{background:#4d4d4d}
.btn-ghost{border:2px solid var(--white);background:transparent}

/* header */
.site-header{position:absolute;left:0;top:0;width:1200px;height:95px;background:rgba(255,255,255,.93);z-index:5}
.brand{position:absolute;left:160px;top:24px;display:flex;align-items:center;gap:10px}
.brand-dot{width:44px;height:44px;border-radius:50%;background:var(--blue);flex:none}
.brand-name{font-size:24px;line-height:23px;font-weight:400;color:var(--blue);letter-spacing:.5px;text-transform:uppercase;white-space:nowrap}
.main-nav{position:absolute;right:157px;top:0;height:95px;display:flex;align-items:center;gap:18px}
.main-nav a{font-size:11px;font-weight:500;color:#333;text-decoration:none;letter-spacing:.2px;white-space:nowrap}
.main-nav a.active{color:var(--blue)}

/* hero */
.hero{position:absolute;left:0;top:0;width:1200px;height:605px;background:linear-gradient(160deg,#5c4a3a 0%,#3d2f25 40%,#2a211c 70%,#4a3a2e 100%)}
.hero-shade{position:absolute;inset:0;background:linear-gradient(90deg,rgba(0,0,0,.35),rgba(0,0,0,.1))}
.hero-kicker{position:absolute;left:160px;top:255px;font-family:"Roboto Condensed",sans-serif;font-size:20px;color:var(--white);letter-spacing:.5px}
.hero-title{position:absolute;left:158px;top:275px;font-family:"Roboto Condensed",sans-serif;font-weight:700;font-size:54px;color:var(--white);letter-spacing:.3px}
.hero-copy{position:absolute;left:160px;top:338px;width:680px;font-size:13px;line-height:17px;color:var(--white)}

/* welcome */
.eyebrow{font-size:13px;color:var(--ink);letter-spacing:.5px}
.section-title{font-size:34px;font-weight:500;color:var(--ink)}
.service{position:absolute;top:828px;width:300px;text-align:center}
.service-icon{width:126px;height:126px;border-radius:50%;margin:0 auto;display:flex;align-items:center;justify-content:center;border:3px solid #3a3a3a}
.service-icon.is-blue{border-color:var(--blue)}
.service h3{margin-top:28px;font-size:18px;font-weight:500;color:var(--ink)}
.service p{margin-top:10px;padding:0 10px}

/* video */
.video-band{position:absolute;left:0;top:1187px;width:1200px;height:350px;background:linear-gradient(120deg,#3f3f3f,#2b2b2b 55%,#3a3a3a)}
.video-title{position:absolute;top:1345px;width:1200px;text-align:center;font-size:24px;color:var(--white);font-weight:300}
.video-duration{position:absolute;top:1374px;width:1200px;text-align:center;font-size:12px;color:#ccc;letter-spacing:.5px}

/* rockstars */
.rock-photo{position:absolute;left:210px;top:1572px;width:320px;height:320px;border-radius:50%;background:radial-gradient(circle at 40% 35%,#5a6a8a,#2c3048 55%,#16182a)}
.rock-title{position:absolute;left:555px;top:1600px;font-size:38px;font-weight:500;color:var(--ink)}
.rock-copy{position:absolute;left:557px;top:1655px;width:480px}

/* stats */
.stats{position:absolute;left:0;top:1950px;width:1200px;height:312px;background:var(--blue)}
.stat{position:absolute;top:2015px;width:230px;text-align:center}
.stat-ring{width:104px;height:104px;border:3px solid var(--white);border-radius:50%;margin:0 auto;display:flex;align-items:center;justify-content:center;font-size:24px;color:var(--white)}
.stat-label{margin-top:18px;font-size:14px;font-weight:500;color:var(--white)}
.stat-divider{position:absolute;top:1995px;width:1px;height:175px;background:rgba(255,255,255,.35)}

/* partners */
.partner{position:absolute;width:205px;height:150px;border:1px solid var(--line);display:flex;align-items:center;justify-content:center}
.partner-mark{width:70px;height:50px;background:#7a7a7a;border-radius:6px}

/* clients */
.clients{position:absolute;left:0;top:2800px;width:1200px;height:312px;background:linear-gradient(120deg,#3d3d3d,#2c2c2c 60%,#3a3a3a)}
.quote-mark{position:absolute;font-family:Georgia,serif;font-size:110px;line-height:1;color:rgba(255,255,255,.35)}
.client-quote{position:absolute;left:170px;top:2912px;width:860px;text-align:center;color:#ddd;font-size:12px;line-height:17px}
.avatar{position:absolute;left:582px;top:2962px;width:36px;height:36px;border-radius:50%;background:linear-gradient(#8a9bb0,#4c5b70);border:2px solid var(--white)}

/* social */
.social-ring{position:absolute;width:44px;height:44px;border-radius:50%;border:2px solid}
.card{position:absolute;top:3257px;width:275px;height:185px;border:2px solid;background:var(--white)}
.card-media{height:68px;margin:8px 8px 0}
.card p{font-size:9px;line-height:12px;padding:6px 8px 0}
.card-bar{position:absolute;left:0;bottom:0;width:100%;height:26px;display:flex;align-items:center;gap:6px;padding-left:10px;font-size:9px;color:var(--white)}
.card-bar span.dot{width:14px;height:14px;border-radius:50%;background:var(--white)}

/* footer */
.site-footer{position:absolute;left:0;top:3512px;width:1200px;height:200px;background:var(--charcoal)}
.foot-nav a{display:block;font-size:11px;font-weight:500;color:var(--white);text-decoration:none;line-height:22px}
.foot-nav a.active{color:var(--blue)}
.newsletter-input{position:absolute;left:782px;top:3547px;width:258px;height:36px;background:var(--white);font-size:11px;color:#888;padding:12px 10px}
.foot-social{position:absolute;top:3653px;width:26px;height:26px;border-radius:50%;border:1px solid #bbb}
.copyright{position:absolute;left:0;top:3712px;width:1200px;height:38px;background:var(--blue);display:flex;align-items:center;justify-content:center;font-size:11px;color:var(--white);letter-spacing:.4px}
</style>
</head>
<body>

<!-- Hero -->
<section class="hero" role="img" aria-label="Photo of business executives seated around a long roundtable lunch in a wood-panelled room">
  <div class="hero-shade"></div>
</section>
<header class="site-header">
  <div class="brand"><span class="brand-dot"></span><span class="brand-name">Quillfern<br>Media</span></div>
  <nav class="main-nav">
    <a class="active">HOME</a><a>ROCKSTARS</a><a>LOCAL LEGENDS</a><a>UNSUNG HEROES</a><a>THE BAND</a><a>THE PARTNERS</a><a>YOU &amp; DORIAN PELLHAM</a>
  </nav>
</header>
<div class="hero-kicker">A FULL SERVICE EVENTS AND</div>
<h1 class="hero-title">CONFERENCES COMPANY</h1>
<p class="hero-copy">Vivamus nibh imperdiet, sollicitudin est ut, tempus nulla. Quisque id nisl vel metus consequat facilisis condimentum vitae est. Nullam lacinia.</p>
<a class="btn btn-blue" style="left:162px;top:395px;width:122px;height:38px">Get in touch</a>
<a class="btn btn-ghost" style="left:298px;top:395px;width:122px;height:38px">Know more</a>

<!-- Welcome -->
<div class="abs center eyebrow" style="top:672px;width:1200px">WELCOME TO</div>
<h2 class="abs center section-title" style="top:688px;width:1200px">QUILLFERN MEDIA</h2>
<p class="abs center" style="left:160px;top:738px;width:880px">Vivamus iaculis rhoncus augue sed fermentum. Interdum et malesuada fames ac ante ipsum primis in faucibus. Nunc orci lectus, molestie eu viverra pulvinar, dignissim vitae ligula. Ut venenatis tristique purus. Integer quis arcu sem. Vestibulum ante ipsum primis in faucibus orci luctus et ultrices posuere cubilia Curae; Fusce a fringilla nulla. Mauris sodales interdum eros. Donec dapibus felis odio, quis faucibus erat interdum vel Vestibulum ante ipsum primis.</p>

<div class="service" style="left:142px">
  <div class="service-icon is-blue">
    <svg width="56" height="56" viewBox="0 0 56 56" fill="#1bbde0"><polygon points="28,4 52,16 4,16"/><rect x="6" y="18" width="44" height="4"/><rect x="10" y="24" width="6" height="20"/><rect x="20" y="24" width="6" height="20"/><rect x="30" y="24" width="6" height="20"/><rect x="40" y="24" width="6" height="20"/><rect x="4" y="46" width="48" height="6"/></svg>
  </div>
  <h3>BANKING</h3>
  <p>Vivamus iaculis rhoncus augue sed fermentum. Interdum et malesuada fames ac ante ipsum primis in faucibus. Nunc orci lectus, molestie eu viverra pulvinar.</p>
</div>
<div class="service" style="left:450px">
  <div class="service-icon">
    <svg width="60" height="56" viewBox="0 0 60 56"><path d="M30 52 C10 38 4 28 4 18 A12 12 0 0 1 30 12 A12 12 0 0 1 56 18 C56 28 50 38 30 52Z" fill="#3a3a3a"/><polyline points="8,28 20,28 25,18 31,38 36,26 52,26" fill="none" stroke="#fff" stroke-width="3"/></svg>
  </div>
  <h3>HEALTH</h3>
  <p>Vivamus iaculis rhoncus augue sed fermentum. Interdum et malesuada fames ac ante ipsum primis in faucibus. Nunc orci lectus, molestie eu viverra pulvinar.</p>
</div>
<div class="service" style="left:752px">
  <div class="service-icon">
    <svg width="60" height="58" viewBox="0 0 60 58" fill="#3a3a3a"><rect x="28" y="2" width="4" height="8"/><path d="M16 24 A14 14 0 0 1 44 24Z"/><rect x="12" y="24" width="36" height="4"/><rect x="4" y="30" width="52" height="4"/><rect x="8" y="36" width="5" height="14"/><rect x="18" y="36" width="5" height="14"/><rect x="28" y="36" width="5" height="14"/><rect x="38" y="36" width="5" height="14"/><rect x="47" y="36" width="5" height="14"/><rect x="2" y="52" width="56" height="5"/></svg>
  </div>
  <h3>GOVERNMENT SECTOR</h3>
  <p>Vivamus iaculis rhoncus augue sed fermentum. Interdum et malesuada fames ac ante ipsum primis in faucibus. Nunc orci lectus, molestie eu viverra pulvinar.</p>
</div>
<a class="btn btn-blue" style="left:237px;top:1077px;width:112px;height:34px">Read more</a>
<a class="btn btn-dark" style="left:544px;top:1077px;width:112px;height:34px">Read more</a>
<a class="btn btn-dark" style="left:851px;top:1077px;width:112px;height:34px">Read more</a>

<!-- Corporate video -->
<section class="video-band" role="img" aria-label="Dimmed photo of a conference room as the video cover"></section>
<svg class="abs" style="left:0;top:1430px" width="1200" height="112" viewBox="0 0 1200 112">
  <polygon points="0,107 1200,12 1200,112 0,112" fill="#fff"/>
  <line x1="0" y1="107" x2="1200" y2="12" stroke="#1bbde0" stroke-width="5"/>
</svg>
<svg class="abs" style="left:568px;top:1270px" width="64" height="64" viewBox="0 0 64 64"><circle cx="32" cy="32" r="29" fill="none" stroke="#1bbde0" stroke-width="3"/><polygon points="26,20 46,32 26,44" fill="none" stroke="#1bbde0" stroke-width="3"/></svg>
<div class="video-title">WATCH OUR CORPORATE VIDEO</div>
<div class="video-duration">DURATION : 6:30</div>

<!-- Rockstars -->
<div class="rock-photo" role="img" aria-label="Photo of a speaker presenting on a lit stage to an engaged audience"></div>
<h2 class="rock-title">ROCKSTARS</h2>
<div class="rock-copy">
  <p>Vivamus iaculis rhoncus augue sed fermentum. Interdum et malesuada fames ac ante ipsum primis in faucibus. Nunc orci lectus, molestie eu viverra pulvinar, dignissim vitae ligula.</p>
  <p style="margin-top:14px">Ut venenatis tristique purus. Integer quis arcu sem. Vestibulum ante ipsum primis in faucibus orci luctus et ultrices posuere cubilia Curae; Fusce a fringilla nulla. Mauris sodales interdum eros. Donec dapibus felis odio quis faucibus erat interdum.</p>
</div>
<a class="btn btn-dark" style="left:557px;top:1775px;width:112px;height:32px">Read more</a>

<!-- Stats -->
<section class="stats"></section>
<svg class="abs" style="left:0;top:2170px" width="1200" height="94" viewBox="0 0 1200 94"><polygon points="0,92 1200,5 1200,94 0,94" fill="#fff"/></svg>
<div class="stat-divider" style="left:370px"></div>
<div class="stat-divider" style="left:600px"></div>
<div class="stat-divider" style="left:830px"></div>
<div class="stat" style="left:140px"><div class="stat-ring">120+</div><div class="stat-label">CORPORATE EVENTS DONE</div></div>
<div class="stat" style="left:370px"><div class="stat-ring">80+</div><div class="stat-label">CONSULTATIONS OFFERED</div></div>
<div class="stat" style="left:600px"><div class="stat-ring">150+</div><div class="stat-label">HAPPY CLIENTS</div></div>
<div class="stat" style="left:830px"><div class="stat-ring">50+</div><div class="stat-label">HAPPY EMPLOYEES</div></div>

<!-- Partners -->
<h2 class="abs center section-title" style="top:2280px;width:1200px">OUR PARTNERS</h2>
<p class="abs center" style="left:170px;top:2337px;width:860px">Ut venenatis tristique purus. Integer quis arcu sem. Vestibulum ante ipsum primis in faucibus orci luctus et ultrices posuere cubilia Curae; Fusce a fringilla nulla. Mauris sodales interdum eros. Donec dapibus felis odio quis faucibus erat interdum.</p>
<div class="partner" style="left:157px;top:2410px"><span class="partner-mark"></span></div>
<div class="partner" style="left:384px;top:2410px"><span class="partner-mark"></span></div>
<div class="partner" style="left:610px;top:2410px"><span class="partner-mark"></span></div>
<div class="partner" style="left:835px;top:2410px"><span class="partner-mark"></span></div>
<div class="partner" style="left:157px;top:2580px"><span class="partner-mark"></span></div>
<div class="partner" style="left:384px;top:2580px"><span class="partner-mark"></span></div>
<div class="partner" style="left:610px;top:2580px"><span class="partner-mark"></span></div>
<div class="partner" style="left:835px;top:2580px"><span class="partner-mark"></span></div>

<!-- Clients -->
<section class="clients" role="img" aria-label="Dimmed photo of a conference audience behind the testimonial"></section>
<svg class="abs" style="left:0;top:2990px" width="1200" height="126" viewBox="0 0 1200 126"><polygon points="0,120 1200,5 1200,126 0,126" fill="#fff"/><line x1="0" y1="120" x2="1200" y2="5" stroke="#1bbde0" stroke-width="5"/></svg>
<div class="quote-mark" style="left:160px;top:2862px">&ldquo;</div>
<div class="quote-mark" style="left:978px;top:2935px">&rdquo;</div>
<div class="abs center" style="top:2845px;width:1200px;font-size:13px;color:var(--blue)">SOME WORDS OF</div>
<h2 class="abs center" style="top:2858px;width:1200px;font-size:36px;font-weight:500;color:var(--white)">OUR CLIENTS</h2>
<p class="client-quote">Suspendisse sit amet suscipit ante. Nam erat arcu, efficitur at rutrum ac, vehicula id libero. Aenean venenatis vel urna vitae elementum. Ut porttitor in quam in convallis. Duis eu ultrices risus, id commodo ligula. Donec finibus nibh id ornare lobortis Ut lobortis accumsan.</p>
<div class="avatar" role="img" aria-label="Client portrait"></div>
<svg class="abs" style="left:530px;top:2973px" width="140" height="14" viewBox="0 0 140 14"><polyline points="8,2 3,7 8,12" fill="none" stroke="#fff" stroke-width="2"/><polyline points="132,2 137,7 132,12" fill="none" stroke="#fff" stroke-width="2"/></svg>
<div class="abs center" style="top:3006px;width:1200px;font-size:11px;font-weight:500;color:var(--white)">Naledi Ferreira</div>

<!-- Social wall -->
<h2 class="abs center section-title" style="top:3130px;width:1200px;font-size:32px">SOCIAL LIVE WALL!</h2>
<div class="social-ring" style="left:523px;top:3186px;border-color:var(--fb)"></div>
<div class="social-ring" style="left:578px;top:3186px;border-color:var(--blue)"></div>
<div class="social-ring" style="left:633px;top:3186px;border-color:var(--red)"></div>

<div class="card" style="left:160px;border-color:var(--blue)">
  <div style="display:flex;gap:8px;padding:10px 8px 0">
    <span style="width:40px;height:40px;border-radius:50%;border:1px solid var(--line);flex:none"></span>
    <div><div style="font-size:11px;color:var(--ink)">Nunc semper augue</div><div style="font-size:8px;color:var(--muted)">@quill_notes</div><div style="font-size:9px;line-height:12px;color:var(--text)">Suspendisse sit amet suscipit ante. Nam erat arcu.</div></div>
  </div>
  <p>Suspendisse sit amet <span style="color:var(--blue)">suscipit ante</span>. Nam erat arcu, efficitur at rutrum ac, vehicula id libero. Aenean <span style="color:var(--blue)">venenatis</span> vel urna vitae elementum ut porttitor <span style="color:var(--blue)">in quam</span>.</p>
  <div class="card-bar" style="background:var(--blue)"><span class="dot"></span>Tweeted 7 hrs. • 30 mins ago</div>
</div>
<div class="card" style="left:462px;border-color:var(--fb)">
  <div class="card-media" role="img" aria-label="Photo of an audience at a conference" style="background:linear-gradient(90deg,#3a3a3a,#777,#2e2e2e)"></div>
  <p>Suspendisse sit amet suscipit ante. Nam erat arcu, efficitur at rutrum ac, vehicula id libero. Aenean venenatis vel urna vitae elementum ut porttitor in quam.</p>
  <div class="card-bar" style="background:var(--fb)"><span class="dot"></span>Posted 10 hrs. • 5 mins ago</div>
</div>
<div class="card" style="left:762px;border-color:var(--red)">
  <div class="card-media" role="img" aria-label="Video still of a speaker" style="background:linear-gradient(90deg,#7a4a30,#c08060,#5a3a2a)"></div>
  <p>Suspendisse sit amet suscipit ante. Nam erat arcu, efficitur at rutrum ac, vehicula id libero.<br><span style="color:var(--red)">Aenean venenatis vel.</span></p>
  <div class="card-bar" style="background:var(--red)"><span class="dot"></span>Uploaded 1 Weeks • 4 days ago</div>
</div>

<!-- Footer -->
<footer class="site-footer">
  <div class="brand" style="top:30px;left:160px"><span class="brand-dot"></span><span class="brand-name">Quillfern<br>Media</span></div>
  <p class="abs" style="left:160px;top:90px;width:250px;font-size:9px;line-height:12px;color:#ccc">Suspendisse sit amet suscipit ante. Nam erat arcu, efficitur at rutrum ac, vehicula id libero. Aenean venenatis vel urna vitae elementum ut porttitor in quam.</p>
  <nav class="abs foot-nav" style="left:478px;top:30px"><a class="active">HOME</a><a>ROCKSTARS</a><a>LOCAL LEGENDS</a><a>UNSUNG HEROES</a></nav>
  <nav class="abs foot-nav" style="left:615px;top:30px"><a>THE BAND</a><a>THE PARTNERS</a><a>YOU &amp; DORIAN PELLHAM</a></nav>
</footer>
<div class="newsletter-input">ENTER YOUR EMAIL ID</div>
<a class="btn btn-blue" style="left:782px;top:3590px;width:118px;height:32px">Subscribe</a>
<div class="foot-social" style="left:160px"></div>
<div class="foot-social" style="left:192px"></div>
<div class="foot-social" style="left:224px"></div>
<div class="copyright">© COPYRIGHT 2018 · QUILLFERN MEDIA &nbsp;&nbsp; | &nbsp;&nbsp; ALL RIGHTS RESERVED</div>

</body>
</html>
```